Optometrist/Eye Care Clinic Business card with new logo attached

We are a small, independent eye care clinic in Canada. We have recently updated our logo (as attached), and would like a professional, modern and health care oriented business card to highlight our office details and our optometrist. We'd like to incorporate the blue colours as seen on our logo.

Target Market(s)

demographic: age 35-65 male/female equal

Industry/Entity Type

Health Care

Contact Information for Business Card

Name of clinic: "Marrow Bend Eye Care Optometry"

Font styles to use
Sans Serif

Colors
0355a3

Requirements
Must have
• our website: marrowbendeyecare.com
• Dr Lena Quorvik
• Optometrist
• 217-392 E Halvering Ave
• Vancouver BC V6R 3J8
• P: 604-319-2058
• E: info@marrowbendeyecare.com
Nice to have
• front side: logo/name of clinic as seen on logo attached and website
• backside: logo on the left side, and name/title/address/phone/email

```html
<!DOCTYPE html>
<html lang="en">
<head>
<meta charset="utf-8">
<title>Marrow Bend Eye Care Optometry – Business Card</title>
<link href="https://fonts.googleapis.com/css2?family=Roboto:wght@400;500;700&display=swap" rel="stylesheet">
<style>
  :root {
    --page-bg: #e9ecf0;
    --card-white: #ffffff;
    --brand-blue: #0355a3;
    --brand-blue-light: #4a86bf;
    --brand-teal: #2a86b4;
    --brand-navy: #1d4a6e;
    --web-blue: #3d9cc7;
    --text-white: #ffffff;
  }
  * { box-sizing: border-box; margin: 0; padding: 0; }
  html, body { width: 1200px; height: 800px; overflow: hidden; }
  body {
    background: var(--page-bg);
    font-family: "Roboto", Arial, sans-serif;
    display: flex;
    flex-direction: column;
    align-items: center;
    justify-content: center;
    gap: 40px;
  }
  .card {
    position: relative;
    width: 600px;
    height: 343px;
    border-radius: 24px;
    background: var(--card-white);
    overflow: hidden;
    box-shadow: 0 6px 20px rgba(0,0,0,0.18);
  }
  /* front */
  .card-front {
    display: flex;
    flex-direction: column;
    align-items: center;
    justify-content: center;
  }
  .brand {
    display: flex;
    flex-direction: column;
    align-items: center;
    gap: 14px;
  }
  .brand-dot {
    width: 70px;
    height: 70px;
    border-radius: 50%;
    background: var(--brand-teal);
  }
  .brand-name {
    font-family: "Roboto", Arial, sans-serif;
    font-weight: 400;
    color: var(--brand-teal);
    text-transform: uppercase;
    text-align: center;
    letter-spacing: 4px;
    line-height: 1.35;
    font-size: 17px;
    max-width: 260px;
  }
  .website {
    margin-top: 34px;
    color: var(--web-blue);
    font-size: 15px;
  }
  /* back */
  .card-back .sweep {
    position: absolute;
    inset: 0;
  }
  .card-back .brand {
    position: absolute;
    left: 40px;
    top: 60px;
    width: 240px;
  }
  .contact {
    position: absolute;
    right: 36px;
    top: 120px;
    text-align: right;
    color: var(--text-white);
    font-size: 14.5px;
    line-height: 1.45;
  }
  .contact .doctor {
    font-weight: 700;
    font-size: 19px;
    letter-spacing: 0.5px;
    text-transform: uppercase;
    line-height: 1.1;
  }
  .contact .title {
    font-weight: 500;
    font-size: 11px;
    letter-spacing: 0.5px;
    text-transform: uppercase;
    margin-bottom: 10px;
  }
  .contact .line-icon {
    display: flex;
    justify-content: flex-end;
    align-items: center;
    gap: 8px;
  }
  .contact svg { width: 15px; height: 15px; flex: none; }
</style>
</head>
<body>

  <section class="card card-front" aria-label="Card front">
    <div class="brand">
      <span class="brand-dot"></span>
      <p class="brand-name">Marrow Bend Eye Care Optometry</p>
    </div>
    <p class="website">www.marrowbendeyecare.com</p>
  </section>

  <section class="card card-back" aria-label="Card back">
    <svg class="sweep" viewBox="0 0 600 343" width="600" height="343" aria-hidden="true">
      <defs>
        <linearGradient id="blueSweep" x1="0" y1="1" x2="1" y2="0">
          <stop offset="0" stop-color="#5b91c6"/>
          <stop offset="0.45" stop-color="#0355a3"/>
          <stop offset="1" stop-color="#0355a3"/>
        </linearGradient>
      </defs>
      <circle cx="716" cy="440" r="486" fill="none" stroke="#2a72ab" stroke-width="6"/>
      <circle cx="700" cy="440" r="470" fill="url(#blueSweep)"/>
    </svg>

    <div class="brand">
      <span class="brand-dot"></span>
      <p class="brand-name">Marrow Bend Eye Care Optometry</p>
    </div>

    <div class="contact">
      <p class="doctor">Dr Lena Quorvik</p>
      <p class="title">Optometrist</p>
      <p>217-392 E Halvering Ave</p>
      <p>Vancouver BC V6R 3J8</p>
      <p class="line-icon">604-319-2058
        <svg viewBox="0 0 16 16" aria-label="Phone"><circle cx="8" cy="8" r="8" fill="#fff"/><rect x="5.5" y="3.5" width="5" height="9" rx="1" fill="none" stroke="#0355a3" stroke-width="1.3"/><circle cx="8" cy="10.8" r="0.7" fill="#0355a3"/></svg>
      </p>
      <p class="line-icon">info@marrowbendeyecare.com
        <svg viewBox="0 0 16 16" aria-label="Email"><circle cx="8" cy="8" r="8" fill="#fff"/><rect x="4" y="5" width="8" height="6" rx="0.6" fill="none" stroke="#0355a3" stroke-width="1.2"/><path d="M4.3 5.4 8 8.3 11.7 5.4" fill="none" stroke="#0355a3" stroke-width="1.2"/></svg>
      </p>
    </div>
  </section>

</body>
</html>
```